Business Card Design with existing logo

TealHeron provides inspirational leadership training and coaching for corporate executives. We focus on being challenging, humorous and compassionate, providing the right mix of support and push for individuals and teams to improve their knowledge and performance. The colour purple is essential to the design. We already have a logo we are very happy with - we are curious to see what can be done to come across in a professional, high standard way that sets us apart. Ideally the design should include the photo of Lise-Britt
Target Market(s)
HR/ Senior Management 500 - 1500 employees
Industry/Entity Type
Leadership
Contact Information for Business Card
TealHeron Coaching Ltd
Inspirational leadership
Lise-Britt Holmgaard Pennick
Leadership coach and trainer
Telephone: +44 1632 960 418
Mobile: +44 7700 900 562
e-mail: lisebritt@tealheroncoaching.example
www.tealheroncoaching.example
Requirements
Must have
- The existing logo
Picture of Lise-Britt

```html
<!DOCTYPE html>
<html lang="en">
<head>
<meta charset="utf-8">
<title>TealHeron Coaching Ltd – Business Card</title>
<link rel="stylesheet" href="https://fonts.googleapis.com/css2?family=Exo+2:wght@500;600&family=Open+Sans:wght@300;400;700&display=swap">
<style>
  :root {
    --purple: #6a3d9a;
    --purple-light: #8a63b8;
    --ink: #2b2b2b;
    --grey: #6e6e6e;
    --paper: #ffffff;
    --backdrop: #e9e6ee;
    --photo-top: #c9c9c9;
    --photo-bottom: #8f8f8f;
  }
  * { box-sizing: border-box; margin: 0; padding: 0; }
  html, body { width: 1200px; height: 960px; overflow: hidden; }
  body {
    background: var(--backdrop);
    font-family: "Open Sans", Arial, sans-serif;
    position: relative;
  }
  .card {
    position: absolute;
    left: 250px;
    width: 700px;
    height: 400px;
    box-shadow: 0 10px 28px rgba(40, 20, 60, 0.18);
  }
  .card--front { top: 60px; background: var(--paper); }
  .card--back { top: 500px; background: var(--purple); }

  /* Front */
  .brand { position: absolute; left: 48px; top: 52px; display: flex; align-items: center; }
  .brand__dot {
    width: 96px; height: 96px; border-radius: 50%;
    background: var(--purple); flex: none;
  }
  .brand__text { margin-left: 18px; }
  .brand__name {
    font-family: "Exo 2", Arial, sans-serif;
    font-weight: 600; font-size: 36px; letter-spacing: 1px;
    text-transform: uppercase; color: var(--purple); line-height: 1;
  }
  .brand__tagline {
    margin-top: 8px; font-size: 13px; font-weight: 400;
    letter-spacing: 5px; text-transform: uppercase; color: var(--purple-light);
  }
  .person { position: absolute; right: 272px; top: 182px; text-align: right; }
  .person__name {
    font-family: "Exo 2", Arial, sans-serif; font-weight: 600;
    font-size: 26px; letter-spacing: 1px; text-transform: uppercase;
    color: var(--purple); line-height: 1.1;
  }
  .person__role {
    margin-top: 4px; font-size: 11px; font-weight: 700;
    letter-spacing: 0.5px; text-transform: uppercase; color: var(--ink); line-height: 1.45;
  }
  .contact {
    position: absolute; right: 272px; top: 268px; text-align: right;
    font-size: 14px; font-weight: 300; color: var(--grey); line-height: 1.5;
    list-style: none;
  }
  .photo {
    position: absolute; left: 458px; top: 150px;
    width: 176px; height: 176px; border-radius: 50%;
    border: 6px solid var(--purple);
    background: linear-gradient(160deg, var(--photo-top), var(--photo-bottom));
  }

  /* Back */
  .back-mark {
    position: absolute; left: 262px; top: 40px;
    width: 176px; height: 176px; border-radius: 50%; background: var(--paper);
  }
  .back-brand { position: absolute; left: 0; right: 0; top: 262px; text-align: center; }
  .back-brand__name {
    font-family: "Exo 2", Arial, sans-serif; font-weight: 600;
    font-size: 30px; letter-spacing: 1px; text-transform: uppercase;
    color: var(--paper); line-height: 1;
  }
  .back-brand__tagline {
    margin-top: 8px; font-size: 11px; letter-spacing: 5px;
    text-transform: uppercase; color: var(--paper);
  }
</style>
</head>
<body>
  <section class="card card--front">
    <div class="brand">
      <div class="brand__dot"></div>
      <div class="brand__text">
        <div class="brand__name">TealHeron Coaching Ltd</div>
        <div class="brand__tagline">Inspirational Leadership</div>
      </div>
    </div>

    <div class="person">
      <div class="person__name">Lise-Britt</div>
      <div class="person__role">Holmgaard Pennick Leadership<br>Coach and Trainer</div>
    </div>

    <ul class="contact">
      <li>Phone: +44 1632 960 418</li>
      <li>Mobile: +44 7700 900 562</li>
      <li>E-Mail:&nbsp; lisebritt@tealheroncoaching.example</li>
      <li>www.tealheroncoaching.example</li>
    </ul>

    <div class="photo" role="img" aria-label="Portrait photo of Lise-Britt Holmgaard Pennick"></div>
  </section>

  <section class="card card--back">
    <div class="back-mark"></div>
    <div class="back-brand">
      <div class="back-brand__name">TealHeron Coaching Ltd</div>
      <div class="back-brand__tagline">Inspirational Leadership</div>
    </div>
  </section>
</body>
</html>
```